CodeVarnaly.com Redesign

Please read the notes and see the site-map attached.
Updates

We are looking for something highly creative. Please provide your best work. Best of luck and thank you very much for your hard work!

Reason: I am seeing good designs but I am not seeing great designs. I really need a design that is unique and is going to wow me. No one is required to stick to the existing color schemes etc. You are free to use other colors etc. I am seeing a lot of the same colors that are used on the site now.

Target Market(s)

Business and entrepreneurs mainly. People looking to build applications, software or launch web or mobile tech products.

Colors

Designer to choose colors to be used in the design.

Requirements
Must have
• See my attached html file.
Nice to have
Should not have
• No sure

```html
<!DOCTYPE html>
<html lang="en">
<head>
<meta charset="utf-8">
<title>CodeVarnaly.com</title>
<link href="https://fonts.googleapis.com/css2?family=Open+Sans:wght@300;400;600;700&display=swap" rel="stylesheet">
<style>
:root{
  --green:#8cc63f;
  --green-dark:#6fa52a;
  --ink:#333a40;
  --muted:#8a9096;
  --navy:#1f3447;
  --navy-deep:#17293a;
  --band:#f3f4f5;
  --line:#e2e4e6;
  --white:#ffffff;
}
*{box-sizing:border-box;margin:0;padding:0}
html,body{width:691px;height:1200px;overflow:hidden;background:var(--white)}
body{font-family:"Open Sans",Arial,sans-serif;color:var(--ink)}
.page{width:691px;height:1200px;position:relative}

/* header */
.site-header{height:74px;display:flex;align-items:center;padding:0 26px;justify-content:space-between}
.brand{display:flex;align-items:center;gap:8px;font-weight:600;font-size:19px;color:var(--ink)}
.brand-dot{width:22px;height:22px;border-radius:50%;background:var(--green)}
.main-nav{display:flex;align-items:center;gap:4px;font-size:9px;font-weight:600;letter-spacing:.3px}
.main-nav a{color:var(--ink);text-decoration:none;padding:7px 10px}
.main-nav a.active{background:var(--green);color:var(--white)}
.main-nav .quote{border:1px solid var(--green);color:var(--green);margin-left:10px;padding:5px 8px}

/* hero */
.hero{position:relative;height:301px;overflow:hidden}
.hero-photo{position:absolute;inset:0;background:linear-gradient(100deg,#c9b7ad 0%,#e6e1dc 35%,#b8ada4 60%,#dcdcd6 100%)}
.hero-title{position:absolute;top:58px;left:0;right:0;text-align:center;color:var(--white);text-shadow:0 1px 3px rgba(0,0,0,.35)}
.hero-title h1{font-size:26px;font-weight:600;line-height:1.2}
.hero-title p{font-size:20px;font-weight:400;margin-top:4px}
.play{position:absolute;left:50%;top:200px;transform:translate(-50%,-50%);width:30px;height:30px;border-radius:50%;background:rgba(30,30,30,.8)}
.arrow{position:absolute;top:198px;width:16px;height:30px;background:rgba(30,30,30,.85)}
.arrow.left{left:0}.arrow.right{right:0}
.arrow svg,.play svg{display:block;margin:auto;height:100%}

/* who */
.who{text-align:center;padding:20px 70px 0;height:180px}
.who h2,.cases h2{font-size:24px;font-weight:300}
.who p{font-size:7.5px;line-height:1.6;color:var(--muted);margin-top:8px}
.btn-dark{display:inline-flex;align-items:center;margin-top:12px;background:var(--navy);color:var(--white);font-size:8px;font-weight:600;letter-spacing:.5px}
.btn-dark .ic{width:16px;height:20px;background:var(--navy-deep);display:flex;align-items:center;justify-content:center}
.btn-dark span{padding:5px 12px}

/* services */
.services{background:var(--band);height:253px;padding-top:26px;text-align:center}
.services h2{color:var(--green);font-size:20px;font-weight:400;letter-spacing:.5px}
.service-list{display:flex;justify-content:center;gap:46px;margin-top:24px}
.service{width:160px}
.service svg{height:44px}
.service h3{font-size:13px;font-weight:400;margin-top:6px}
.service p{font-size:7px;line-height:1.55;color:var(--muted);margin-top:6px}
.btn-green{display:inline-block;margin-top:10px;background:var(--green);color:var(--white);font-size:6.5px;font-weight:600;padding:5px 12px}

/* cases */
.cases{height:203px;padding-top:22px;text-align:center}
.case-list{display:flex;gap:30px;padding:0 70px;margin-top:14px;text-align:left}
.case{flex:1;display:flex;gap:10px}
.avatar{width:40px;height:40px;border-radius:50%;background:linear-gradient(#b89a82,#6d5a4e);flex:none}
.case p{font-size:7px;line-height:1.6;color:var(--muted)}
.case cite{display:block;font-style:normal;font-size:7.5px;color:var(--ink);margin-top:5px}

/* footer */
.site-footer{background:var(--navy);height:155px;padding:22px 70px 0;display:flex;gap:40px}
.footer-col{flex:1}
.footer-col h4{color:var(--white);font-size:11px;font-weight:600;letter-spacing:.5px;margin-bottom:8px}
.footer-col li{list-style:none;font-size:7px;line-height:1.6;color:#b8c3cc}
.footer-bar{background:var(--navy-deep);height:25px;display:flex;align-items:center;justify-content:space-between;padding:0 70px;font-size:6.5px;color:#8fa0ae}
.social{display:flex;gap:5px}
.social i{width:10px;height:10px;border-radius:50%;background:#8fa0ae;display:block}
</style>
</head>
<body>
<div class="page">
  <header class="site-header">
    <div class="brand"><span class="brand-dot"></span>CodeVarnaly</div>
    <nav class="main-nav">
      <a class="active" href="#">HOME</a><a href="#">ABOUT US</a><a href="#">OUR WORK</a><a href="#">SERVICES</a><a href="#">REACH US</a><a class="quote" href="#">FREE QUOTE</a>
    </nav>
  </header>

  <section class="hero">
    <div class="hero-photo" role="img" aria-label="Photo of a man and a woman working together at a laptop in a bright office"></div>
    <div class="hero-title">
      <h1>Donec scelerisque neque lorus Praesent</h1>
      <p>Mauris vel luctus vitae felis vestibulum</p>
    </div>
    <div class="play"><svg viewBox="0 0 30 30" width="30"><path d="M12 9l9 6-9 6z" fill="#fff"/></svg></div>
    <div class="arrow left"><svg viewBox="0 0 16 30" width="16"><path d="M10 10l-5 5 5 5" stroke="#fff" stroke-width="2" fill="none"/></svg></div>
    <div class="arrow right"><svg viewBox="0 0 16 30" width="16"><path d="M6 10l5 5-5 5" stroke="#fff" stroke-width="2" fill="none"/></svg></div>
  </section>

  <section class="who">
    <h2>Who We Are</h2>
    <p>Nunc tempus felis vitae urna vivamus porttitor neque at volutpat iaculis purus nisi eleifend libero a tempus libero fusce feugiat nibh morbi. Nam mauris viverra in gravida eu mattis in, ante blandit quis orci lectus ipsum dapibus venenatis elementum nulla tempor. Vestibulum ligula lectus, hendrerit sit amet posuere in, imperdiet eget lorem, integer pulvinar magna nisi amet.</p>
    <p>Curabitur iaculis tempus ante. Curabitur vel nisl at ante magna malesuada ultrices ut nisl erat fermentum sed congue id euismod in elit fusce ultricies orci ut. Aliquam suscipit leo cursus sodales, velit id scelerisque et luctus ipsum in proin fusce nisi tellus commodo ac gravida.</p>
    <a class="btn-dark" href="#"><span class="ic"><svg width="6" height="8" viewBox="0 0 6 8"><path d="M1 1l4 3-4 3" stroke="#fff" fill="none"/></svg></span><span>WHAT WE DO</span></a>
  </section>

  <section class="services">
    <h2>OUR SERVICES</h2>
    <div class="service-list">
      <div class="service">
        <svg viewBox="0 0 44 44" width="44"><rect x="6" y="8" width="32" height="24" rx="2" fill="none" stroke="#333a40" stroke-width="2"/><path d="M18 16l-4 4 4 4M26 16l4 4-4 4" stroke="#333a40" stroke-width="2" fill="none"/><path d="M14 38h16" stroke="#333a40" stroke-width="2"/></svg>
        <h3>Web Development</h3>
        <p>Etiam non nunc vel diam convallis tempus lorem ac nisi. Sed sem risus mattis vitae tempus quis, fermentum at tortor magna dis parturient montes, nascetur ridiculus mus.</p>
        <a class="btn-green" href="#">READ MORE</a>
      </div>
      <div class="service">
        <svg viewBox="0 0 44 44" width="44"><rect x="14" y="4" width="16" height="32" rx="3" fill="none" stroke="#333a40" stroke-width="2"/><circle cx="22" cy="31" r="1.5" fill="#333a40"/><path d="M8 40h28" stroke="#333a40" stroke-width="2"/></svg>
        <h3>Mobile App Development</h3>
        <p>Etiam non nunc vel diam convallis tempus lorem ac nisi. Sed sem risus mattis vitae tempus quis, fermentum at tortor magna dis parturient montes, nascetur ridiculus mus.</p>
        <a class="btn-green" href="#">READ MORE</a>
      </div>
      <div class="service">
        <svg viewBox="0 0 44 44" width="44"><circle cx="22" cy="22" r="13" fill="none" stroke="#333a40" stroke-width="2"/><circle cx="22" cy="22" r="5" fill="#333a40"/><path d="M22 4v6M22 34v6M4 22h6M34 22h6" stroke="#333a40" stroke-width="2"/></svg>
        <h3>Software Development</h3>
        <p>Etiam non nunc vel diam convallis tempus lorem ac nisi. Sed sem risus mattis vitae tempus quis, fermentum at tortor magna dis parturient montes, nascetur ridiculus mus.</p>
        <a class="btn-green" href="#">READ MORE</a>
      </div>
    </div>
  </section>

  <section class="cases">
    <h2>Case Studies</h2>
    <div class="case-list">
      <div class="case">
        <div class="avatar" role="img" aria-label="Portrait photo of a client"></div>
        <div>
          <p>Lorem ipsum dolor sit amet, consectetur adipiscing elit, sed do eiusmod tempor incididunt ut labore et dolore magna aliqua. Ut enim ad minim veniam quis nostrud exercitation ullamco laboris nisi ut aliquip ex ea commodo consequat duis aute irure.</p>
          <cite>Daniel Whitmore, Partner-Ashgrove Partners</cite>
        </div>
      </div>
      <div class="case">
        <div class="avatar" role="img" aria-label="Portrait photo of a client"></div>
        <div>
          <p>We taught with a really creative team and we are thrilled with the results. Their attention to detail and friendly approach made the whole process smooth and we would happily recommend them to any business planning a product launch.</p>
          <cite>Peter Langford, CEO GreenBasket Inc</cite>
        </div>
      </div>
    </div>
  </section>

  <footer>
    <div class="site-footer">
      <div class="footer-col"><h4>COMPANY</h4><ul><li>Home</li><li>About Us</li><li>What We Do</li><li>Who We Are</li><li>Testimonials</li></ul></div>
      <div class="footer-col"><h4>FEATURES</h4><ul><li>Aliquam nec erat</li><li>In porta cursus</li><li>Curabitur facilisis</li><li>Ligula augue</li><li>Maecenas accumsan</li></ul></div>
      <div class="footer-col"><h4>SERVICES</h4><ul><li>Web Development</li><li>Mobile App Development</li><li>Custom Software Development</li><li>User Experience Design</li></ul></div>
      <div class="footer-col"><h4>CONTACT US</h4><ul><li>CodeVarnaly.com</li><li>1420 Harbour Street #12</li><li>Riverton, WA 98000</li><li>Phone: +1 000 555 0142</li><li>Email: hello@codevarnaly.com</li><li>Skype: codevarnaly</li></ul></div>
    </div>
    <div class="footer-bar">
      <span>© 2014 Company Name. All rights reserved | Terms of Use</span>
      <span class="social"><i></i><i></i><i></i><i></i><i></i></span>
    </div>
  </footer>
</div>
</body>
</html>
```